Accounting services

Looking for a Business card & Logo design

company name - LUMEN ACCOUNTING & TAXATION SOLUTIONS

name - Corwin Pell

position - Accountant / Business Consultant

email - "undecided"

Tel : (868) 512-4873 / (868) 587-2196

**PUT THESE TO THE BACK**
Accounting - VAT * INCOME/CORP TAX * RETURNS

REGISTRATION - VAT * NIS * Company Registration/Business Plan

Industry/Entity Type

Business

```html
<!DOCTYPE html>
<html lang="en">
<head>
<meta charset="utf-8">
<title>Lumen Accounting &amp; Taxation Solutions — Business Card</title>
<link href="https://fonts.googleapis.com/css2?family=Marcellus&display=swap" rel="stylesheet">
<style>
  :root {
    --canvas: #e6e4df;
    --card-deep: #0b4466;
    --card-mid: #0e5a85;
    --card-light: #13699a;
    --ink: #f4f7fa;
    --ink-soft: #d7e4ee;
    --band: #eef0f2;
    --band-shade: #cfd4d8;
  }
  * { margin: 0; padding: 0; box-sizing: border-box; }
  html, body {
    width: 1200px; height: 885px; overflow: hidden;
    background: var(--canvas);
    font-family: "Marcellus", "Times New Roman", serif;
    color: var(--ink);
  }
  .canvas { position: relative; width: 1200px; height: 885px; }

  .card {
    position: absolute;
    width: 620px; height: 354px;
    background: radial-gradient(ellipse at 45% 35%, var(--card-light) 0%, var(--card-mid) 45%, var(--card-deep) 100%);
    box-shadow: 0 10px 28px rgba(0,0,0,.22);
    overflow: hidden;
  }
  .card--front { left: 60px; top: 70px; }
  .card--back  { left: 520px; top: 462px; }

  /* Front */
  .front__company {
    position: absolute; left: 60px; top: 44px;
    font-size: 31px; line-height: 36px; letter-spacing: 1.5px;
  }
  .front__rule {
    position: absolute; left: 0; right: 0; top: 134px;
    height: 1px; background: var(--ink);
  }
  .front__person {
    position: absolute; left: 110px; top: 114px;
    padding: 0 12px;
    background: var(--card-mid);
    background: radial-gradient(ellipse at 50% 50%, var(--card-light), var(--card-mid));
  }
  .front__name { font-size: 30px; letter-spacing: 1.5px; line-height: 40px; }
  .front__role { font-size: 14px; color: var(--ink-soft); letter-spacing: .4px; margin-top: 2px; }
  .front__contact {
    position: absolute; left: 300px; top: 200px;
    font-size: 17px; line-height: 23px; text-align: left;
  }
  .front__contact .email { font-size: 19px; }
  .front__band {
    position: absolute; left: 0; right: 0; bottom: 0; height: 54px;
    background: linear-gradient(180deg, var(--band) 0%, var(--band) 70%, var(--band-shade) 100%);
  }

  /* Back */
  .back__content {
    position: absolute; left: 0; right: 0; top: 46px;
    text-align: center;
  }
  .back__company { font-size: 28px; line-height: 33px; letter-spacing: 1.5px; }
  .back__heading { font-size: 27px; margin-top: 26px; letter-spacing: .5px; }
  .back__heading--caps { font-size: 23px; letter-spacing: 1px; margin-top: 16px; }
  .back__list { font-size: 13.5px; letter-spacing: .6px; color: var(--ink-soft); margin-top: 6px; }
</style>
</head>
<body>
<main class="canvas">
  <section class="card card--front" aria-label="Business card front">
    <h1 class="front__company">LUMEN ACCOUNTING<br>&amp; TAXATION SOLUTIONS</h1>
    <div class="front__rule"></div>
    <div class="front__person">
      <div class="front__name">CORWIN PELL</div>
      <div class="front__role">Accountant / Business Consultant</div>
    </div>
    <div class="front__contact">
      <div>(868) 512-4873</div>
      <div>(868) 587-2196</div>
      <div class="email">mail@lumenaccounting.com</div>
    </div>
    <div class="front__band"></div>
  </section>

  <section class="card card--back" aria-label="Business card back">
    <div class="back__content">
      <h2 class="back__company">LUMEN ACCOUNTING<br>&amp; TAXATION SOLUTIONS</h2>
      <div class="back__heading">Accounting -</div>
      <div class="back__list">VAT - INCOME/CORP TAX - RETURNS</div>
      <div class="back__heading back__heading--caps">REGISTRATION -</div>
      <div class="back__list">VAT - NIS - Company Registration/Business Plan</div>
    </div>
  </section>
</main>
</body>
</html>
```